Hollis Ironworks Business Card

We need a business card design for a new small metal fabrication business in rural NSW, Australia.

The business (Hollis Ironworks) is owner operated by a man with the initials RB - much of the branding comes from this name.

Hollis Ironworks designs, engineers, repairs and manufactures a range of custom, quality metal works including vehicle trays, agricultural machinery impliments, trailers, wood splitters, fire pits, furniture etc.

The brand position focuses on custom work of the highest quality.

Business card design should show quality, attention to detail and stand out among a mass of business cards.

Logos are in the files

The grey color may be changed on the logo if required to stand out more.

There is an image attached of a simple card that is liked because it is clean, clear, simple, masculine and effective. It says 'quality'. As most of the work we do is custom it would be good to have the business card speak to this.

Target Market(s)

Rural and regional based Australians. Primarily adult male 25-60 yrs. Primary production / rural / travelling lifestyle.

Industry/Entity Type

Metal Fabrication

Contact Information for Business Card

The words 'custom quality fabrications' would be great somewhere perhaps on the backside (not on the information side)
Name
title
Phone: 0491 538 274 and (02) 7342 9185
email: info@hollisiw.com.au
www.hollisiw.com.au

address (2 lines)

Requirements
Nice to have
• Background colour should be very navy blue or black.
Should not have
• NO orange and blue combinations.
• Navy is OK

```html
<!DOCTYPE html>
<html lang="en">
<head>
<meta charset="utf-8">
<title>Hollis Ironworks Business Card</title>
<link href="https://fonts.googleapis.com/css2?family=Arimo:wght@400;700&display=swap" rel="stylesheet">
<style>
  :root {
    --backdrop: #3a3230;
    --card: #161617;
    --card-edge: #0c0c0d;
    --steel: #b9bcbf;
    --steel-dark: #55585b;
    --green: #5cc13c;
    --white: #f2f2f2;
    --divider: #6a6a6a;
  }
  * { margin: 0; padding: 0; box-sizing: border-box; }
  html, body {
    width: 1200px; height: 864px; overflow: hidden;
    background: var(--backdrop);
    font-family: "Arimo", Arial, sans-serif;
  }
  .stage { position: relative; width: 1200px; height: 864px; }
  .card {
    position: absolute;
    width: 500px; height: 286px;
    background: var(--card);
    border: 1px solid var(--card-edge);
    box-shadow: 0 10px 28px rgba(0,0,0,.45);
  }
  .card-back { left: 70px; top: 130px; }
  .card-front { left: 630px; top: 440px; }

  .back-brand {
    position: absolute; left: 0; right: 0; top: 96px;
    display: flex; align-items: center; justify-content: center; gap: 12px;
  }
  .brand-square { width: 22px; height: 22px; background: var(--steel-dark); }
  .back-brand .brand-name {
    font-weight: 700; font-size: 30px; letter-spacing: 2px;
    color: var(--steel-dark); text-transform: uppercase;
  }
  .back-web {
    position: absolute; left: 0; right: 0; top: 176px;
    text-align: center; font-size: 14px; letter-spacing: 3.5px;
    color: var(--steel-dark);
  }

  .front-brand {
    position: absolute; left: 150px; top: 78px;
    display: flex; align-items: center; gap: 10px;
  }
  .front-brand .brand-square { background: var(--green); width: 26px; height: 26px; }
  .front-brand .brand-name {
    font-weight: 700; font-size: 30px; letter-spacing: 1.5px;
    color: var(--steel); text-transform: uppercase;
  }
  .person {
    position: absolute; right: 268px; top: 170px; text-align: right;
  }
  .person-name { color: var(--green); font-size: 17px; letter-spacing: .5px; }
  .person-title { color: var(--white); font-size: 15px; margin-top: 4px; }
  .divider {
    position: absolute; left: 244px; top: 166px; width: 1px; height: 70px;
    background: var(--divider);
  }
  .contacts {
    position: absolute; left: 258px; top: 166px; list-style: none;
  }
  .contacts li {
    display: flex; align-items: center; gap: 10px;
    color: var(--white); font-size: 14px; height: 23px;
  }
  .contacts svg { width: 14px; height: 14px; fill: var(--green); flex: none; }
</style>
</head>
<body>
<main class="stage">
  <section class="card card-back" aria-label="Card back">
    <div class="back-brand">
      <span class="brand-square"></span>
      <span class="brand-name">Hollis Ironworks</span>
    </div>
    <p class="back-web">www.hollisiw.com.au</p>
  </section>

  <section class="card card-front" aria-label="Card front">
    <div class="front-brand">
      <span class="brand-square"></span>
      <span class="brand-name">Hollis Ironworks</span>
    </div>
    <div class="person">
      <p class="person-name">RYAN BELL</p>
      <p class="person-title">President</p>
    </div>
    <span class="divider"></span>
    <ul class="contacts">
      <li>
        <svg viewBox="0 0 24 24" aria-hidden="true"><path d="M6.6 10.8a15.1 15.1 0 0 0 6.6 6.6l2.2-2.2c.3-.3.7-.4 1-.2 1.1.4 2.3.6 3.6.6.6 0 1 .4 1 1V20c0 .6-.4 1-1 1A17 17 0 0 1 3 4c0-.6.4-1 1-1h3.5c.6 0 1 .4 1 1 0 1.3.2 2.5.6 3.6.1.3 0 .7-.2 1z"/></svg>
        0491 538 274
      </li>
      <li>
        <svg viewBox="0 0 24 24" aria-hidden="true"><path d="M6.6 10.8a15.1 15.1 0 0 0 6.6 6.6l2.2-2.2c.3-.3.7-.4 1-.2 1.1.4 2.3.6 3.6.6.6 0 1 .4 1 1V20c0 .6-.4 1-1 1A17 17 0 0 1 3 4c0-.6.4-1 1-1h3.5c.6 0 1 .4 1 1 0 1.3.2 2.5.6 3.6.1.3 0 .7-.2 1z"/></svg>
        (02) 7342 9185
      </li>
      <li>
        <svg viewBox="0 0 24 24" aria-hidden="true"><path d="M2 5h20v14H2z M2 5l10 8 10-8" /></svg>
        info@hollisiw.com.au
      </li>
    </ul>
  </section>
</main>
</body>
</html>
```